Premium modern eliquids labels 84.5 x 80 mm

I am looking for modern graphics for the labels of a new eliquid line that will have 4 different types of eliquids. It will have a tobacco one (brown colours maybe), a fruity one (bright colours maybe), a minty one (green colours maybe) and a creamy one (beige colours maybe).
I will need one of them to see how the design is, that design will have to be adapted to the other 3 colours of the label.
The brand logo is attached. I also attached a sample of what is mandatory to write on the label, you can change size, place and font of what is written, the only thing that cannot be reduced is the yellow parts. I attach the bottle that we will use.The size of the label is 84.5 x 80 mm (base x height).

Target Market(s)

vapers

Requirements
Must have
• My project must have one of the labels.

```html
<!DOCTYPE html>
<html lang="it">
<head>
<meta charset="utf-8">
<title>Zenith Aroma – etichette 20 ml</title>
<link rel="stylesheet" href="https://fonts.googleapis.com/css2?family=Lexend:wght@500;800&family=Archivo:wght@700;800&family=PT+Sans+Narrow:wght@400;700&display=swap">
<style>
  :root {
    --page: #ffffff;
    --badge-yellow: #fbc53a;
    --badge-ink: #1b1b1b;
  }
  * { box-sizing: border-box; margin: 0; padding: 0; }
  html, body { width: 1200px; height: 1200px; overflow: hidden; background: var(--page); }
  .sheet { position: relative; width: 1200px; height: 1200px; }

  .label {
    position: absolute; width: 502px; height: 474px; overflow: hidden;
    border: 1px solid var(--edge);
    font-family: "PT Sans Narrow", "Arial Narrow", sans-serif;
    color: var(--ink);
  }
  .label--tobacco { left: 91px; top: 111px;
    --edge: #5b2e0c; --ink: #fffdf3; --brand: #f4f0cc; --title: #ffffff;
    --bg: linear-gradient(135deg, #b5622f 0%, #7a3c0a 30%, #d49f5d 55%, #c0773d 75%, #4e2a12 100%); }
  .label--fruit { left: 615px; top: 111px;
    --edge: #4e3a7a; --ink: #1a0f2e; --brand: #1a0f2e; --title: #1a0f2e;
    --bg: linear-gradient(135deg, #8fae5a 0%, #4e3a7a 22%, #c7468a 45%, #ff7a6a 62%, #f9d54a 80%, #4e3a7a 100%); }
  .label--mint { left: 91px; top: 622px;
    --edge: #1f6a46; --ink: #0f4a30; --brand: #0f4a30; --title: #0f4a30;
    --bg: linear-gradient(135deg, #aeeac8 0%, #46b483 28%, #76dea6 52%, #1f8a5a 74%, #aeeac8 100%); }
  .label--cream { left: 615px; top: 622px;
    --edge: #d8cfa8; --ink: #8a8566; --brand: #86815f; --title: #86815f;
    --bg: linear-gradient(135deg, #f6eec0 0%, #fffbe7 30%, #ede0a3 58%, #fff6d4 80%, #e4d6a0 100%); }

  .label__art { position: absolute; inset: 0; background: var(--bg); }

  .brand {
    position: absolute; left: 110px; top: 60px; width: 282px; text-align: center;
    font-family: "Lexend", sans-serif; font-weight: 800; color: var(--brand); line-height: 1;
  }
  .brand__main { display: block; font-size: 46px; letter-spacing: 1px; }
  .brand__sub { display: block; font-size: 15px; letter-spacing: 9px; margin-top: 6px; }

  .flavour {
    position: absolute; left: 0; width: 502px; text-align: center;
    font-family: "Lexend", sans-serif; font-weight: 500; color: var(--title);
  }
  .flavour__name { top: 398px; font-size: 29px; }
  .flavour__volume { top: 448px; font-size: 15px; left: 5px; letter-spacing: .5px; }

  .legal {
    position: absolute; writing-mode: vertical-rl; transform: rotate(180deg);
    font-size: 8.4px; line-height: 1; white-space: nowrap;
  }
  .legal b { font-weight: 700; }
  .legal--lot { left: 8px; bottom: 12px; }
  .legal--ingredients { left: 22px; bottom: 12px; }
  .legal--storage { left: 36px; bottom: 270px; }
  .legal--maker { left: 460px; bottom: 190px; }
  .legal--contact { left: 474px; bottom: 190px; }

  .disposal-icons { position: absolute; left: 445px; top: 292px; width: 50px; height: 24px; color: var(--ink); }

  .badge {
    position: absolute; background: var(--badge-yellow); color: var(--badge-ink);
    font-family: "Archivo", sans-serif; font-weight: 800; text-align: center; line-height: 1;
  }
  .badge--wide { left: 422px; width: 72px; font-size: 10.5px; padding: 2px 0; }
  .badge--code { left: 425px; width: 50px; font-size: 12px; padding: 4px 0; letter-spacing: .5px; }
  .badge-note {
    position: absolute; left: 425px; width: 50px; text-align: center;
    font-family: "Archivo", sans-serif; font-weight: 700; font-size: 7.5px; color: var(--ink);
  }
  .r1 { top: 333px; } .n1 { top: 361px; } .c1 { top: 369px; }
  .r2 { top: 404px; } .n2 { top: 432px; } .c2 { top: 440px; }
</style>
</head>
<body>
<main class="sheet">

  <!-- repeated label block -->
  <section class="label label--tobacco">
    <div class="label__art" role="img" aria-label="Abstract pattern of flowing ribbons, rings and bubbles in tobacco browns"></div>
    <div class="brand"><span class="brand__main">ZENITH</span><span class="brand__sub">AROMA</span></div>
    <p class="flavour flavour__name">TOBACCO</p>
    <p class="flavour flavour__volume">20 ML NET</p>
    <p class="legal legal--lot">L.SH20 - <b>001-PES</b>- D.PROD <b>22-04-2022</b> D.SC <b>21-04-2024</b> <b>ISTRUZIONI D'USO:</b> Agitare bene prima dell'utilizzo</p>
    <p class="legal legal--ingredients"><b>INGREDIENTI:</b> GLICOLE PROPILENICO SOSTANZE AROMATIZZANTI &nbsp; Diluire nelle percentuali consigliate sul nostro sito.</p>
    <p class="legal legal--storage">Conservare in luogo fresco e asciutto</p>
    <p class="legal legal--maker">PRODOTTO E CONFEZIONATO DA Lumenio srl Via Lago 18 10100 Torino</p>
    <p class="legal legal--contact">Pi:00000000000 Tel. +39 000 0000000 info@lumenio.it</p>
    <svg class="disposal-icons" viewBox="0 0 50 24" fill="none" stroke="currentColor" stroke-width="1.2" aria-hidden="true">
      <path d="M4 18 L10 7 L16 18 Z"/><path d="M8 4 l2 3 -3 1"/>
      <path d="M32 10 h10 l-1.5 12 h-7 Z"/><circle cx="44" cy="3" r="2"/><path d="M44 6 v8 M44 14 l-2 8 M44 14 l2 8 M41 8 l3 1"/>
    </svg>
    <div class="badge badge--wide r1">RACCOLTA<br>PLASTICA</div>
    <div class="badge-note n1">ETICHETTA</div>
    <div class="badge badge--code c1">PAP 5</div>
    <div class="badge badge--wide r2">RACCOLTA<br>PLASTICA</div>
    <div class="badge-note n2">FLACONE</div>
    <div class="badge badge--code c2">PET 1</div>
  </section>

  <section class="label label--fruit">
    <div class="label__art" role="img" aria-label="Abstract pattern of flowing ribbons, rings and bubbles in bright purple, pink, coral, yellow and green"></div>
    <div class="brand"><span class="brand__main">ZENITH</span><span class="brand__sub">AROMA</span></div>
    <p class="flavour flavour__name">FRUIT</p>
    <p class="flavour flavour__volume">20 ML NET</p>
    <p class="legal legal--lot">L.SH20 - <b>001-PES</b>- D.PROD <b>22-04-2022</b> D.SC <b>21-04-2024</b> <b>ISTRUZIONI D'USO:</b> Agitare bene prima dell'utilizzo</p>
    <p class="legal legal--ingredients"><b>INGREDIENTI:</b> GLICOLE PROPILENICO SOSTANZE AROMATIZZANTI &nbsp; Diluire nelle percentuali consigliate sul nostro sito.</p>
    <p class="legal legal--storage">Conservare in luogo fresco e asciutto</p>
    <p class="legal legal--maker">PRODOTTO E CONFEZIONATO DA Lumenio srl Via Lago 18 10100 Torino</p>
    <p class="legal legal--contact">Pi:00000000000 Tel. +39 000 0000000 info@lumenio.it</p>
    <svg class="disposal-icons" viewBox="0 0 50 24" fill="none" stroke="currentColor" stroke-width="1.2" aria-hidden="true">
      <path d="M4 18 L10 7 L16 18 Z"/><path d="M8 4 l2 3 -3 1"/>
      <path d="M32 10 h10 l-1.5 12 h-7 Z"/><circle cx="44" cy="3" r="2"/><path d="M44 6 v8 M44 14 l-2 8 M44 14 l2 8 M41 8 l3 1"/>
    </svg>
    <div class="badge badge--wide r1">RACCOLTA<br>PLASTICA</div>
    <div class="badge-note n1">ETICHETTA</div>
    <div class="badge badge--code c1">PAP 5</div>
    <div class="badge badge--wide r2">RACCOLTA<br>PLASTICA</div>
    <div class="badge-note n2">FLACONE</div>
    <div class="badge badge--code c2">PET 1</div>
  </section>

  <section class="label label--mint">
    <div class="label__art" role="img" aria-label="Abstract pattern of flowing ribbons, rings and bubbles in mint greens"></div>
    <div class="brand"><span class="brand__main">ZENITH</span><span class="brand__sub">AROMA</span></div>
    <p class="flavour flavour__name">MINT</p>
    <p class="flavour flavour__volume">20 ML NET</p>
    <p class="legal legal--lot">L.SH20 - <b>001-PES</b>- D.PROD <b>22-04-2022</b> D.SC <b>21-04-2024</b> <b>ISTRUZIONI D'USO:</b> Agitare bene prima dell'utilizzo</p>
    <p class="legal legal--ingredients"><b>INGREDIENTI:</b> GLICOLE PROPILENICO SOSTANZE AROMATIZZANTI &nbsp; Diluire nelle percentuali consigliate sul nostro sito.</p>
    <p class="legal legal--storage">Conservare in luogo fresco e asciutto</p>
    <p class="legal legal--maker">PRODOTTO E CONFEZIONATO DA Lumenio srl Via Lago 18 10100 Torino</p>
    <p class="legal legal--contact">Pi:00000000000 Tel. +39 000 0000000 info@lumenio.it</p>
    <svg class="disposal-icons" viewBox="0 0 50 24" fill="none" stroke="currentColor" stroke-width="1.2" aria-hidden="true">
      <path d="M4 18 L10 7 L16 18 Z"/><path d="M8 4 l2 3 -3 1"/>
      <path d="M32 10 h10 l-1.5 12 h-7 Z"/><circle cx="44" cy="3" r="2"/><path d="M44 6 v8 M44 14 l-2 8 M44 14 l2 8 M41 8 l3 1"/>
    </svg>
    <div class="badge badge--wide r1">RACCOLTA<br>PLASTICA</div>
    <div class="badge-note n1">ETICHETTA</div>
    <div class="badge badge--code c1">PAP 5</div>
    <div class="badge badge--wide r2">RACCOLTA<br>PLASTICA</div>
    <div class="badge-note n2">FLACONE</div>
    <div class="badge badge--code c2">PET 1</div>
  </section>

  <section class="label label--cream">
    <div class="label__art" role="img" aria-label="Abstract pattern of flowing ribbons, rings and bubbles in soft cream and beige"></div>
    <div class="brand"><span class="brand__main">ZENITH</span><span class="brand__sub">AROMA</span></div>
    <p class="flavour flavour__name">CREAM</p>
    <p class="flavour flavour__volume">20 ML NET</p>
    <p class="legal legal--lot">L.SH20 - <b>001-PES</b>- D.PROD <b>22-04-2022</b> D.SC <b>21-04-2024</b> <b>ISTRUZIONI D'USO:</b> Agitare bene prima dell'utilizzo</p>
    <p class="legal legal--ingredients"><b>INGREDIENTI:</b> GLICOLE PROPILENICO SOSTANZE AROMATIZZANTI &nbsp; Diluire nelle percentuali consigliate sul nostro sito.</p>
    <p class="legal legal--storage">Conservare in luogo fresco e asciutto</p>
    <p class="legal legal--maker">PRODOTTO E CONFEZIONATO DA Lumenio srl Via Lago 18 10100 Torino</p>
    <p class="legal legal--contact">Pi:00000000000 Tel. +39 000 0000000 info@lumenio.it</p>
    <svg class="disposal-icons" viewBox="0 0 50 24" fill="none" stroke="currentColor" stroke-width="1.2" aria-hidden="true">
      <path d="M4 18 L10 7 L16 18 Z"/><path d="M8 4 l2 3 -3 1"/>
      <path d="M32 10 h10 l-1.5 12 h-7 Z"/><circle cx="44" cy="3" r="2"/><path d="M44 6 v8 M44 14 l-2 8 M44 14 l2 8 M41 8 l3 1"/>
    </svg>
    <div class="badge badge--wide r1">RACCOLTA<br>PLASTICA</div>
    <div class="badge-note n1">ETICHETTA</div>
    <div class="badge badge--code c1">PAP 5</div>
    <div class="badge badge--wide r2">RACCOLTA<br>PLASTICA</div>
    <div class="badge-note n2">FLACONE</div>
    <div class="badge badge--code c2">PET 1</div>
  </section>

</main>
</body>
</html>
```